Lumen Gin Label Design modern Contemporary

Label size 4”x10” or 10.16cm x 25.4cm

I’m not to concerned with the content as I can swap out the wording and upc and qr etc that’s why I mention it’s all fpo. What I’m looking for is cool design ideas that tie into art or painting or the name lumen. The one I pick will be based on over all designs so no need to stress on content.
I require a Label for a new Gin.

I have started the creative and have attached samples but i want something that POP's more and adds more colour the label will wrap around the bottle as in the example attached. this can be contemporary, Abstract or geometrical. PLEASE note the attaches is only examples and can be changed totally its just toggle an idea of the layout. i have some ideas that i have attached. I don't know if i want to go with a pattern as in some examples or the painted as in others. I just want to ensure that the LOGO is clearly visible. PLEASE NOTE!!!!! The still (machine) in the example can be removed at the moment i don't think looks good with it. Also the wording, QR and UPC are just FPO. Sizing on the Logo and name can also be changed to accommodate design. I am looking for some cool creative ideas they by no means need to be like i have shown if you have a cool innovative idea lets see it!! Would be great if the art could be integrated in the front and carry over to the end of the label to create a flow but also not necessary. Full creative is up to you. Thank you !

AGAIN THE LABEL ATTACHED IS JUST AN EXAMPLE IM NOT HAPPY WITH IT OR HOWIT LOOKS SO AGAIN ITS JUST FOR REFERNCE OF POSITIONING!

Below is a description of the product:

Lumen Gin is a premium alcohol spirit brand focused on the arts community. Made from carefully crafted premium botanicals and distilled through a proprietary process it’s a clean carefully crafted Gin. !00% produced from farm to table with Canadian farmers and premium Grain from 100% wheat used in the finest pastries to provide a crisp delicate and smooth base to this finely crafted gin. As an artist creates their art with paint on a lumen we have created this fine Gin with our carefully selected botanicals and premium spirit.

Target Market(s)

Artists, Trendy

Industry/Entity Type

Spirits , Alcohol

Requirements
Must have
• I have attached the logo in Black And White Sizecan be changed to suit design both words and logo
Should not have
• Do not need to add the machine i have on the example

```html
<!DOCTYPE html>
<html lang="en">
<head>
<meta charset="utf-8">
<title>Lumen Gin – Wraparound Label</title>
<link href="https://fonts.googleapis.com/css2?family=Montserrat:wght@300;400;500;600;700&display=swap" rel="stylesheet">
<style>
  :root {
    --backdrop: #e3e6e3;
    --white: #ffffff;
    --ink: #1f1f1f;
    --rule: #9a9a9a;
    --accent: #b5401c;
    --orange: #ff6a13;
    --yellow: #fdb813;
    --navy: #1b1c7a;
    --pink: #ff3fc4;
    --cyan: #9ef0e8;
    --green: #5df07a;
    --red: #f5333f;
  }
  * { margin: 0; padding: 0; box-sizing: border-box; }
  html, body { width: 1200px; height: 596px; overflow: hidden; background: var(--backdrop); }
  .canvas { position: relative; width: 1200px; height: 596px; font-family: "Montserrat", sans-serif; }

  .label { position: absolute; left: 95px; top: 84px; width: 1013px; height: 405px; overflow: hidden; }
  .label-pattern {
    position: absolute; inset: 0;
    background: linear-gradient(100deg,
      var(--orange) 0%, var(--yellow) 14%, var(--navy) 28%, var(--pink) 42%,
      var(--cyan) 52%, var(--orange) 62%, var(--navy) 72%, var(--yellow) 82%,
      var(--pink) 91%, var(--green) 100%);
  }

  .front-panel { position: absolute; left: 202px; top: 0; width: 204px; height: 405px; }
  .front-panel svg { position: absolute; inset: 0; }

  .brand { position: absolute; left: 0; width: 204px; text-align: center; color: var(--ink); }
  .brand-name { top: 196px; font-size: 33px; font-weight: 500; letter-spacing: 1px; line-height: 1; }
  .brand-gin { top: 238px; font-size: 24px; font-weight: 500; letter-spacing: 1px; line-height: 1; }
  .tagline { position: absolute; left: 0; top: 275px; width: 204px; text-align: center;
    color: var(--accent); font-size: 9.6px; font-weight: 600; line-height: 12px; letter-spacing: 0.2px; }
  .divider { position: absolute; left: 33px; top: 323px; width: 138px; height: 1px;
    background: linear-gradient(90deg, transparent, var(--ink), transparent); }
  .product-info { position: absolute; left: 0; top: 340px; width: 204px; text-align: center; color: var(--ink); }
  .product-info .origin { font-size: 9.4px; font-weight: 600; line-height: 13px; }
  .product-info .country { font-size: 10.4px; font-weight: 700; line-height: 13px; }
  .product-info .volume { font-size: 9.6px; font-weight: 700; line-height: 14px; }

  .spec-panel { position: absolute; left: 51px; top: 254px; width: 100px; height: 100px; background: var(--white); }
  .spec-box { position: absolute; left: 5px; top: 6px; width: 89px; height: 88px; border: 1px solid var(--rule); }

  .story-panel { position: absolute; left: 710px; top: 101px; width: 278px; height: 278px; background: var(--white); }
  .story-box { position: absolute; left: 5px; top: 6px; width: 267px; height: 267px; border: 1px solid var(--rule);
    padding: 11px 12px 0 12px; }
  .story-text { font-size: 9.6px; font-weight: 400; line-height: 14.7px; color: #3a3a3a; text-align: justify; }
</style>
</head>
<body>
<main class="canvas">
  <section class="label">
    <div class="label-pattern" role="img" aria-label="Colourful geometric mosaic of tiles in orange, yellow, navy, pink, cyan and green with circles, stripes, dots and triangles"></div>

    <div class="front-panel">
      <svg width="204" height="405" viewBox="0 0 204 405">
        <path d="M50 0 H152 V101 H208 V405 H-4 V101 H50 Z" fill="#ffffff"/>
        <path d="M87 7 H122 V107 H171 V399 H33 V107 H87 Z" fill="none" stroke="#9a9a9a" stroke-width="0.8"/>
      </svg>
      <div class="brand brand-name">LUMEN</div>
      <div class="brand brand-gin">GIN</div>
      <p class="tagline">A REBELLIOUS SPIRIT<br>WITH AN UNUSUAL<br>CHARACTER</p>
      <div class="divider"></div>
      <div class="product-info">
        <div class="origin">PRODUCT OF</div>
        <div class="country">CANADA</div>
        <div class="volume">750 mL | 40% ALC./VOL</div>
      </div>
    </div>

    <div class="spec-panel"><div class="spec-box"></div></div>

    <div class="story-panel">
      <div class="story-box">
        <p class="story-text">Lumen Gin is a premium alcohol spirit brand focused on the arts community. Made from carefully crafted premium botanicals and distilled through a proprietary process it’s a clean carefully crafted Gin. 100% produced from farm to table with Canadian farmers and premium Grain from 100% wheat used in the finest pastries to provide a crisp delicate and smooth base to this finely crafted gin. As an artist creates their art with paint on a lumen we have created this fine Gin with our carefully selected botanicals and premium spirit.</p>
      </div>
    </div>
  </section>
</main>
</body>
</html>
```